Australian Legal Practice would like a Web Design

I need a web design for a newly established law practice operating as Brindell Legal.

I would like the business to have an internet presence (via a website) essentially for the purpose of marketing and advertising. As the business grows (hopefully) I may be interested in providing general legal information as a means of establishing goodwill in the community and a easy and user friends contact method through the website.

The essence of the business is personal legal service based on local knowledge and therefore i want the website to present a picture of friendly professionalism, but mostly i want people who to be able to find the contact details of the business

I would like to have a map of the office location, and photos of the front of the office, the staff (me at the moment) and picture of law themed items and featuring the Brindell Legal logo.

The areas of law which Brindell Legal practises in are as follows:

commercial law
business sale and purchases
leases
conveyancing and property law
wills and estates
powers of attorney
general legal advice
succession planning
Updates

Target Market(s)

Potential and existing clients of the firm
Other law firms
Associated stakeholders, i.e. Banks and real estate agents

Industry/Entity Type

Law Firm

Coding

Coded - Design and coding required

Number of Pages Required

2 page

Font styles to use
Sans Serif

Colors
85acd3
33a6d7
0456a4

Requirements
Must have
• Brindell Legal logo
• Map of the office location
• Picture of Ross Kedwick (principal solicitor)
• Picture of the office
• Areas of Practice
• Address of office
• email address: ross.kedwick@brindelllegal-example.com.au
• Physical address: 17 Pellow Road, Hamilton VIC 3300
• Phone number: (03) 5598 4731
• Facsimile number: (03) 5598 4706
• Space for a brief description of the firm and its competitive advantage
• Bar Guild Logo
• Links to the Bar Guild of Victoria
• Link to the practitioner oversight Council
Nice to have
• coded to wordpress format

```html
<!DOCTYPE html>
<html lang="en">
<head>
<meta charset="utf-8">
<title>Brindell Legal</title>
<link href="https://fonts.googleapis.com/css2?family=Open+Sans:wght@400;600;700&display=swap" rel="stylesheet">
<style>
:root{
  --navy:#0a2f96;
  --brand:#1d3f8f;
  --ink:#333333;
  --muted:#555555;
  --soft:#efefef;
  --footer:#ececec;
  --stripe:#d6d6d6;
  --icon:#3a3a3a;
  --white:#ffffff;
}
*{margin:0;padding:0;box-sizing:border-box}
html,body{width:1200px;height:2251px;overflow:hidden}
body{font-family:"Open Sans",Arial,sans-serif;color:var(--ink);background:var(--white);position:relative}

/* header */
.site-header{position:absolute;left:0;top:0;width:1200px;height:92px;background:var(--white)}
.brand{position:absolute;left:176px;top:26px;display:flex;align-items:center;gap:10px;font-size:27px;font-weight:600;color:var(--brand);letter-spacing:.5px}
.brand-mark{width:14px;height:14px;background:var(--brand)}
.social{position:absolute;right:180px;top:32px;display:flex;gap:5px}
.social span{width:27px;height:27px;border-radius:4px;background:#3d3d3d;display:block}

.main-nav{position:absolute;left:0;top:92px;width:1200px;height:50px;background:var(--navy)}
.main-nav ul{list-style:none;display:flex;padding-left:176px;height:50px;align-items:center}
.main-nav li{color:var(--white);font-size:13.5px;margin-right:38px}

.hero{position:absolute;left:0;top:142px;width:1200px;height:414px;
  background:radial-gradient(ellipse at 45% 40%,#b89a78 0%,#6d5544 35%,#3b2e2a 70%,#241c1c 100%)}

/* intro */
.intro{position:absolute;left:0;top:556px;width:1200px;height:464px;background:var(--soft)}
.section-title{position:absolute;left:0;width:1200px;text-align:center;font-weight:400;font-size:29px;color:var(--ink)}
.lead{position:absolute;left:220px;width:760px;text-align:center;font-size:12px;line-height:20px;color:var(--muted)}
.card{position:absolute;top:149px;width:187px}
.card-photo{width:187px;height:166px}
.card h3{font-weight:400;font-size:15px;margin-top:12px;color:var(--ink)}
.card p{font-size:11px;line-height:17px;color:var(--muted);margin-top:5px;height:51px;overflow:hidden}
.card .more{font-size:11px;font-weight:700;margin-top:10px;color:var(--ink)}

/* welcome */
.welcome{position:absolute;left:0;top:1020px;width:1200px;height:259px;
  background:linear-gradient(90deg,#3e3e3e 0%,#5b5b5b 45%,#494949 100%)}
.welcome h2{position:absolute;top:20px;left:0;width:1200px;text-align:center;color:var(--white);font-weight:400;font-size:32px}
.welcome p{position:absolute;top:80px;left:225px;width:750px;text-align:center;color:var(--white);font-size:14px;line-height:22px}
.btn{position:absolute;left:516px;top:189px;width:137px;height:45px;background:var(--white);color:var(--ink);font-size:14px;display:flex;align-items:center;justify-content:center}

/* areas */
.areas{position:absolute;left:0;top:1279px;width:1200px;height:572px;background:var(--white)}
.area{position:absolute;width:272px}
.area-head{display:flex;align-items:center;gap:20px}
.area-icon{width:54px;height:50px;flex:none;background:var(--icon);display:flex;align-items:center;justify-content:center}
.area-head h3{font-weight:400;font-size:18px;color:#222;white-space:nowrap}
.area p{font-size:11.5px;line-height:18.5px;color:var(--muted);margin-top:22px}

/* footer */
.site-footer{position:absolute;left:0;top:1851px;width:1200px;height:400px;background:var(--footer);border-top:13px solid var(--stripe)}
.f-col{position:absolute;top:38px}
.f-col h4{font-size:12px;font-weight:400;letter-spacing:.3px;color:#222}
.about-photo{width:191px;height:78px;margin-top:16px;background:linear-gradient(90deg,#6e3b24,#9a5a37 50%,#5a2f1e)}
.f-text{font-size:11px;line-height:17px;color:#666;margin-top:10px;overflow-wrap:anywhere}
.read{font-size:11px;font-weight:600;color:#333;text-align:right;margin-top:4px}
.links{list-style:none;margin-top:14px;width:200px}
.links li{font-size:10.5px;color:#777;height:24px;line-height:23px;border-bottom:1px solid #d9d9d9;padding-left:14px;position:relative;white-space:nowrap}
.links li::before{content:"›";position:absolute;left:2px;color:#888}
.post h5{font-size:13px;font-weight:400;color:#222;margin-top:16px}
.post .date{font-size:9px;color:#888}
.post p{font-size:10.5px;line-height:16px;color:#666;margin-top:6px;width:185px}
.copyright{position:absolute;left:203px;top:2198px;width:812px;border-top:1px solid #d9d9d9;text-align:center;font-size:10.5px;color:#777;padding-top:22px}
</style>
</head>
<body>

<header class="site-header">
  <div class="brand"><span class="brand-mark"></span>Brindell Legal</div>
  <div class="social" aria-label="Social links"><span></span><span></span><span></span></div>
</header>

<nav class="main-nav">
  <ul>
    <li>Home</li><li>About Us</li><li>Leases</li><li>Immigration</li><li>Estate Planning</li><li>Real Estate</li><li>Legal&nbsp; Service</li><li>Fees-Contact</li>
  </ul>
</nav>

<div class="hero" role="img" aria-label="Photo of scales of justice, gavel, hourglass and law books"></div>

<section class="intro">
  <h2 class="section-title" style="top:40px">Friendly, Professional Local Lawyers</h2>
  <p class="lead" style="top:86px;font-size:11.5px;line-height:18px">Brindell Legal is a newly established Hamilton practice offering personal legal service based on local knowledge, for individuals, businesses, banks and real estate agents.</p>

  <article class="card" style="left:158px">
    <div class="card-photo" role="img" aria-label="Photo of the front of the Brindell Legal office" style="background:linear-gradient(135deg,#c9a26a,#7a4a22 60%,#3a2210)"></div>
    <h3>Our Office</h3>
    <p>Visit us at 17 Pellow Road, Hamilton VIC 3300, in the heart of town.</p>
    <div class="more">More &gt;</div>
  </article>
  <article class="card" style="left:392px">
    <div class="card-photo" role="img" aria-label="Map showing the office location on Pellow Road, Hamilton" style="background:linear-gradient(135deg,#e4e7df,#c9d3c2 55%,#aebfb0)"></div>
    <h3>Find Us</h3>
    <p>Phone (03) 5598 4731 or fax (03) 5598 4706 to make an appointment.</p>
    <div class="more">More &gt;</div>
  </article>
  <article class="card" style="left:621px">
    <div class="card-photo" role="img" aria-label="Photo of principal solicitor Ross Kedwick" style="background:linear-gradient(180deg,#8a5a36,#3a2a24 60%,#1c1a1c)"></div>
    <h3>Ross Kedwick</h3>
    <p>Principal solicitor giving personal advice built on local knowledge.</p>
    <div class="more">More &gt;</div>
  </article>
  <article class="card" style="left:853px">
    <div class="card-photo" role="img" aria-label="Photo of a hand on a law book beside scales" style="background:linear-gradient(135deg,#2a2420,#8a6a44 55%,#d8c29a)"></div>
    <h3>Updates</h3>
    <p>General legal information and news for clients and our community.</p>
    <div class="more">More &gt;</div>
  </article>
</section>

<section class="welcome" role="img" aria-label="Darkened photo of a person writing beside law books">
  <h2>Welcome to BRINDELL LEGAL</h2>
  <p>We are a local Hamilton law practice built on friendly professionalism. Our principal solicitor knows the region, its businesses and its people, so you deal directly with one lawyer who understands your needs. From buying a business to planning your estate, we give clear, practical advice at fair fees, and we are always easy to reach by phone, email or a visit to our office.</p>
  <div class="btn">Read More</div>
</section>

<section class="areas">
  <h2 class="section-title" style="top:24px">Areas of Law</h2>
  <p class="lead" style="top:82px;font-size:13px;line-height:21px">Brindell Legal acts for individuals and businesses across the Western District in commercial and property matters, estate planning, powers of attorney and general legal advice. Call (03) 5598 4731 to discuss your matter.</p>

  <div class="area" style="left:158px;top:193px">
    <div class="area-head"><div class="area-icon"><svg width="26" height="26" viewBox="0 0 26 26" fill="none" stroke="#fff" stroke-width="2"><rect x="3" y="5" width="16" height="18"/><path d="M10 16 L22 4 L24 6 L12 18 L9 19 Z" fill="#fff"/></svg></div><h3>COMMERCIAL LAW</h3></div>
    <p>Contracts, partnerships, company structures and day-to-day commercial advice for local businesses, farmers and sole traders, with clear terms and practical outcomes.</p>
  </div>
  <div class="area" style="left:464px;top:193px">
    <div class="area-head"><div class="area-icon"><svg width="26" height="28" viewBox="0 0 26 28"><text x="13" y="23" text-anchor="middle" fill="#fff" font-family="Open Sans,Arial,sans-serif" font-weight="700" font-size="24">$</text></svg></div><h3>BUSINESS SALES</h3></div>
    <p>Guidance through the sale or purchase of a business, from contract review and due diligence to settlement, so the transfer is smooth for both sides.</p>
  </div>
  <div class="area" style="left:770px;top:193px">
    <div class="area-head"><div class="area-icon"><svg width="28" height="26" viewBox="0 0 28 26" fill="#fff"><rect x="3" y="17" width="4" height="6"/><rect x="9" y="13" width="4" height="10"/><rect x="15" y="9" width="4" height="14"/><rect x="21" y="5" width="4" height="18"/><path d="M3 12 L11 6 L16 8 L25 2" stroke="#fff" stroke-width="2" fill="none"/></svg></div><h3>LEASES</h3></div>
    <p>Preparing, reviewing and negotiating retail, commercial and farm leases for landlords and tenants, including renewals, assignments and lease disputes.</p>
  </div>

  <div class="area" style="left:158px;top:385px">
    <div class="area-head"><div class="area-icon"><svg width="26" height="28" viewBox="0 0 26 28" fill="#fff"><path d="M10 2 a7 7 0 0 1 7 7 c0 5 -7 12 -7 12 s-7 -7 -7 -12 a7 7 0 0 1 7 -7 z"/><circle cx="10" cy="9" r="2.6" fill="#3a3a3a"/><circle cx="20" cy="22" r="3.5"/></svg></div><h3>CONVEYANCING</h3></div>
    <p>Property law and conveyancing for homes, farms and commercial sites, working closely with local banks and real estate agents through to settlement.</p>
  </div>
  <div class="area" style="left:464px;top:385px">
    <div class="area-head"><div class="area-icon"><svg width="28" height="28" viewBox="0 0 28 28"><circle cx="14" cy="14" r="12" fill="#fff"/><path d="M8 14 L12.5 18.5 L20 10" stroke="#3a3a3a" stroke-width="3" fill="none"/></svg></div><h3>WILLS &amp; ESTATES</h3></div>
    <p>Wills, powers of attorney and estate administration, prepared with care so your wishes are clear and your family is supported when it matters most.</p>
  </div>
  <div class="area" style="left:770px;top:385px">
    <div class="area-head"><div class="area-icon"><svg width="28" height="28" viewBox="0 0 28 28" fill="#fff"><circle cx="14" cy="14" r="9"/><g stroke="#fff" stroke-width="4"><line x1="14" y1="2" x2="14" y2="26"/><line x1="2" y1="14" x2="26" y2="14"/><line x1="5.5" y1="5.5" x2="22.5" y2="22.5"/><line x1="22.5" y1="5.5" x2="5.5" y2="22.5"/></g><circle cx="14" cy="14" r="3.5" fill="#3a3a3a"/></svg></div><h3>SUCCESSION</h3></div>
    <p>Succession planning for family businesses and farms, plus general legal advice on everyday questions, so the next generation is ready to take over.</p>
  </div>
</section>

<footer class="site-footer">
  <div class="f-col" style="left:203px;width:200px">
    <h4>ABOUT US</h4>
    <div class="about-photo" role="img" aria-label="Portrait photo of principal solicitor Ross Kedwick in front of bookshelves"></div>
    <p class="f-text">Ross Kedwick, principal solicitor.<br>17 Pellow Road, Hamilton VIC 3300<br>Phone: (03) 5598 4731<br>Fax: (03) 5598 4706<br>ross.kedwick@brindelllegal-example.com.au</p>
    <div class="read">Read More »</div>
  </div>
  <div class="f-col" style="left:509px">
    <h4>QUICK LINKS</h4>
    <ul class="links">
      <li>Home</li><li>About Us</li><li>Areas of Practice</li><li>Commercial Law</li><li>Conveyancing and Property</li><li>Wills and Estates</li><li>Powers of Attorney</li><li>Bar Guild of Victoria</li><li>practitioner oversight Council</li><li>Contact Us</li>
    </ul>
  </div>
  <div class="f-col" style="left:795px;width:200px">
    <h4>LATEST BLOG POSTS</h4>
    <div class="post">
      <h5>Changes to Leases</h5>
      <div class="date">Friday, 10th Oct 2015</div>
      <p>A short guide to what new retail lease rules mean for local tenants.</p>
      <div class="read">Read More »</div>
    </div>
    <div class="post" style="margin-top:10px">
      <h5>Why Make a Will</h5>
      <div class="date">Friday, 10th Oct 2015</div>
      <p>Simple steps to protect your family and plan your estate with confidence.</p>
      <div class="read">Read More »</div>
    </div>
  </div>
</footer>
<div class="copyright">Copyright © 2015 · All Rights Reserved</div>

</body>
</html>
```